"Tour Poster" For First Child!

Hi everyone! My wife and I are expecting our first child and I want to surprise her with an awesome 11x17 "tour poster" commemorating all the things that we did over the past few months while she was pregnant. I've attached some examples of some other tour posters for reference; as well as the "tour dates" text that I'd like included in the flier. This will likely hang in a baby girl's room so it needs to be kid friendly but I don't want it to look too childish.

For the primary graphic, I'm thinking maybe
-a loose cartoon animation of my wife and I (maybe playing in a band? maybe my wife is pregnant in the animation?)
or
-chinese dragons (something kid friendly but still looking cool)
or
-In a car or on a plane like we're on "tour"

(I uploaded 11 photos to help. 3 of me, 3 of my wife, and 5 tour posters. Wanted to give everyone an idea of what we look like to animate; as well as what type of tour posters inspired this)

We both love Pembrook so definitely some bonus points for any animation that is Pemrbook'esque!!

Text:
Baby M's World Tour
Featuring 5607 (written as 5606 with the 6 crossed out and replaced with a 7)

11/9 - Danville, CA (Opening Night)
11/10 - Lake Tahoe, NV SOLD OUT!
11/11 - Lake Tahoe, NV SOLD OUT!
11/12 - Lake Tahoe, NV SOLD OUT!
12/3 - Daly City, CA (Harlow's Market)
12/10 - Los Angeles, CA
12/11 - Anaheim, CA (Wonderhaven)
12/31 - San Mateo, CA (First New Year's Eve)
1/16 - Anaheim, CA (Wonderhaven)
1/17 - Anaheim, CA (Wonderhaven)
1/27 - San Francisco, CA (Copper Kettle Grill)
2/10 - San Jose, CA (First Chinese New Year)
3/3 - San Miguel de Allende, Mexico SOLD OUT!
3/4 - San Miguel de Allende, Mexico SOLD OUT!
3/5 - San Miguel de Allende, Mexico
3/6 - Puerto Vallarta, Mexico SOLD OUT!
3/7 - Puerto Vallarta, Mexico SOLD OUT!
3/29 - Las Vegas, NV SOLD OUT!
3/30 - Las Vegas, NV
3/31 - Las Vegas, NV SOLD OUT!
4/13 - Vancouver, Canada SOLD OUT!
4/14 - Vancouver, Canada
4/15 - Kamloops, Canada
4//16 - Lake Louise, Canada SOLD OUT!
4/17 - Lake Louise, Canada SOLD OUT!
4/18 - Calgary, Canada
4/21 - Monterey, CA
5/2 - New Orleans, LA SOLD OUT!
5/3 - New Orleans, LA SOLD OUT!
5/4 - New Orlean, LA SOLD OUT!
5/5 - New Orleans, LA SOLD OUT!
5//16 - Ojai, CA
5/17 - Anaheim, CA (Wonderhaven)
5/18 - Anaheim, CA (Wonderhaven) SOLD OUT!
5/19 - San Simeon, CA
5/30 - Gilroy, Ca SOLD OUT!
5/31 - Gilroy, Ca SOLD OUT!
6/8 - Corte Madera, CA
6/26 - Pismo Beach, CA
6/27 - Pasadena, CA
6/28 - Indio, CA SOLD OUT!
6/29 - Indio, CA
6/30 - Solvang, CA
7/11 - San Rafael, CA SOLD OUT!
7/12 - San Rafael, CA SOLD OUT!
7/13 - San Rafael, CA SOLD OUT!
8/5 - Castro Valley, CA - SHOWTIME!!!

Requirements
Must have
• big cartoon graphic on top, text at bottom

```html
<!DOCTYPE html>
<html lang="en">
<head>
<meta charset="utf-8">
<title>Baby M's World Tour</title>
<link rel="stylesheet" href="https://fonts.googleapis.com/css2?family=Aldrich&family=Orbitron:wght@600&family=Roboto:wght@400;700&display=swap">
<style>
  :root{
    --blush:#fde6e1;
    --band:#fdf1ef;
    --title-red:#b00a0a;
    --teal:#00abbd;
    --teal-deep:#0f9fb0;
    --dragon-red:#e8462a;
    --dragon-gold:#f6bd1a;
    --date-teal:#1aa7b8;
    --ink:#1c1c1c;
    --faded:#e3c3bb;
    --strike:#5e9e6c;
    --white:#ffffff;
  }
  *{margin:0;padding:0;box-sizing:border-box}
  html,body{width:776px;height:1200px;overflow:hidden;background:var(--white)}
  .poster{position:relative;width:776px;height:1200px;background:var(--white);font-family:"Roboto",sans-serif;color:var(--ink)}
  .header{position:absolute;left:0;top:0;width:776px;height:454px;background:var(--blush);overflow:hidden}
  .dragons{position:absolute;left:0;top:0}
  .title{position:absolute;left:220px;width:340px;top:52px;text-align:center;font-family:"Aldrich",sans-serif;color:var(--title-red);font-size:64px;line-height:76px;letter-spacing:1px;white-space:nowrap}
  .featuring{position:absolute;right:322px;top:253px;font-family:"Orbitron",sans-serif;font-weight:600;font-size:28px;line-height:40px;letter-spacing:0;color:var(--ink);white-space:nowrap}
  .tile{position:absolute;width:60px;height:64px;border-radius:5px;background:var(--teal);color:var(--white);font-family:"Aldrich",sans-serif;font-size:46px;line-height:64px;text-align:center}
  .tile-faded{background:var(--faded);color:var(--white);overflow:hidden}
  .tile-faded svg{position:absolute;left:0;top:0}
  .dates{position:absolute;left:0;top:498px;width:776px;height:612px;
    background:repeating-linear-gradient(to bottom,transparent 0,transparent 30px,var(--band) 30px,var(--band) 53.66px,transparent 53.66px,transparent 55.66px)}
  .col{position:absolute;top:498px;list-style:none;font-size:13.4px}
  .col li{height:27.83px;line-height:27.83px;white-space:nowrap}
  .col-left{left:35px}
  .col-right{left:442px}
  .date{color:var(--date-teal);font-weight:700}
  .date .dash{font-weight:400}
</style>
</head>
<body>
<div class="poster">
  <header class="header">
    <svg class="dragons" width="776" height="454" viewBox="0 0 776 454">
      <defs>
        <linearGradient id="dragonTone" x1="0" y1="0" x2="1" y2="1">
          <stop offset="0" stop-color="var(--dragon-gold)"/>
          <stop offset=".35" stop-color="var(--teal)"/>
          <stop offset=".75" stop-color="var(--teal-deep)"/>
          <stop offset="1" stop-color="var(--dragon-red)"/>
        </linearGradient>
      </defs>
      <path role="img" aria-label="Cartoon Chinese dragon in teal, yellow and red, curling in from the top left" fill="url(#dragonTone)"
        d="M0,0 L132,0 C122,55 100,95 72,125 C100,140 125,160 150,178 C165,190 160,236 136,234 C110,230 88,222 62,214 C42,222 20,234 0,240 Z"/>
      <path role="img" aria-label="Cartoon Chinese dragon in teal, yellow and red, rising from the bottom right" fill="url(#dragonTone)"
        d="M776,205 C742,190 702,198 664,228 L612,250 C618,286 636,298 662,304 C622,330 592,378 610,418 C640,452 706,440 776,384 Z"/>
    </svg>
    <h1 class="title">Baby M's<br>World Tour</h1>
    <div class="featuring">FEATURING</div>
    <div class="tile" style="left:470px;top:243px">7</div>
    <div class="tile" style="left:256px;top:321px">5</div>
    <div class="tile" style="left:328px;top:321px">6</div>
    <div class="tile" style="left:399px;top:321px">0</div>
    <div class="tile tile-faded" style="left:469px;top:321px">6
      <svg width="60" height="64" viewBox="0 0 60 64"><line x1="6" y1="0" x2="54" y2="64" stroke="var(--strike)" stroke-width="6"/></svg>
    </div>
  </header>

  <div class="dates" aria-hidden="true"></div>

  <ul class="col col-left">
    <li><span class="date">11/9<span class="dash"> - </span></span>Danville, CA (Opening Night)</li>
    <li><span class="date">11/10<span class="dash"> - </span></span>Lake Tahoe, NV SOLD OUT!</li>
    <li><span class="date">11/11<span class="dash"> - </span></span>Lake Tahoe, NV SOLD OUT!</li>
    <li><span class="date">11/12<span class="dash"> - </span></span>Lake Tahoe, NV SOLD OUT!</li>
    <li><span class="date">12/3<span class="dash"> - </span></span>Daly City, CA (Harlow's Market)</li>
    <li><span class="date">12/10<span class="dash"> - </span></span>Los Angeles, CA</li>
    <li><span class="date">12/11<span class="dash"> - </span></span>Anaheim, CA (Wonderhaven)</li>
    <li><span class="date">12/31<span class="dash"> - </span></span>San Mateo, CA (First New Year's Eve)</li>
    <li><span class="date">1/16</span> - Anaheim, CA (Wonderhaven)</li>
    <li><span class="date">1/17</span> - Anaheim, CA (Wonderhaven)</li>
    <li><span class="date">1/27</span> - San Francisco, CA (Copper Kettle Grill)</li>
    <li><span class="date">2/10</span> - San Jose, CA (First Chinese New Year)</li>
    <li><span class="date">3/3</span> - San Miguel de Allende, Mexico SOLD OUT!</li>
    <li><span class="date">3/4</span> - San Miguel de Allende, Mexico SOLD OUT!</li>
    <li><span class="date">3/5</span> - San Miguel de Allende, Mexico</li>
    <li><span class="date">3/6</span> - Puerto Vallarta, Mexico SOLD OUT!</li>
    <li><span class="date">3/7</span> - Puerto Vallarta, Mexico SOLD OUT!</li>
    <li><span class="date">3/29</span> - Las Vegas, NV SOLD OUT!</li>
    <li><span class="date">3/30</span> - Las Vegas, NV</li>
    <li><span class="date">3/31</span> - Las Vegas, NV SOLD OUT!</li>
    <li><span class="date">4/13</span> - Vancouver, Canada SOLD OUT!</li>
    <li><span class="date">4/14</span> - Vancouver, Canada</li>
    <li><span class="date">4/15</span> - Kamloops, Canada</li>
  </ul>

  <ul class="col col-right">
    <li><span class="date">4//16</span> - Lake Louise, Canada SOLD OUT!</li>
    <li><span class="date">4/17</span> - Lake Louise, Canada SOLD OUT!</li>
    <li><span class="date">4/18</span> - Calgary, Canada</li>
    <li><span class="date">4/21</span> - Monterey, CA</li>
    <li><span class="date">5/2</span> - New Orleans, LA SOLD OUT!</li>
    <li><span class="date">5/3</span> - New Orleans, LA SOLD OUT!</li>
    <li><span class="date">5/4</span> - New Orlean, LA SOLD OUT!</li>
    <li><span class="date">5/5</span> - New Orleans, LA SOLD OUT!</li>
    <li><span class="date">5//16</span> - Ojai, CA</li>
    <li><span class="date">5/17</span> - Anaheim, CA (Wonderhaven)</li>
    <li><span class="date">5/18</span> - Anaheim, CA (Wonderhaven) SOLD OUT!</li>
    <li><span class="date">5/19</span> - San Simeon, CA</li>
    <li><span class="date">5/30</span> - Gilroy, Ca SOLD OUT!</li>
    <li><span class="date">5/31</span> - Gilroy, Ca SOLD OUT!</li>
    <li><span class="date">6/8</span> - Corte Madera, CA</li>
    <li><span class="date">6/26</span> - Pismo Beach, CA</li>
    <li><span class="date">6/27</span> - Pasadena, CA</li>
    <li><span class="date">6/28</span> - Indio, CA SOLD OUT!</li>
    <li><span class="date">6/29</span> - Indio, CA</li>
    <li><span class="date">6/30</span> - Solvang, CA</li>
    <li><span class="date">7/11</span> - San Rafael, CA SOLD OUT!</li>
    <li><span class="date">7/12</span> - San Rafael, CA SOLD OUT!</li>
    <li><span class="date">7/13</span> - San Rafael, CA SOLD OUT!</li>
    <li><span class="date">8/5</span> - Castro Valley, CA - SHOWTIME!!!</li>
  </ul>
</div>
</body>
</html>
```